high end kitchens , needing new logo and business card design .

im looking a very simple looking design but classy that will stand out , i would like the design to be in the colours black , silver , gold and grey , although all colours dont need to be used in design , back of card to have name on it colin fetterby , address and phone number and website address , maybe fb logo . adrress is 27 moorgate row , kilbrannock , bt41 2qd , 07718492265 , front of the card im open to design , back of card very simple i will want it matt black with silver writing , writing doesnt need to be that big

Target Market(s)

people with kitchen projects .

Industry/Entity Type

Interior Design

Contact Information for Business Card

front of business card hc on it with maybe harbor cabinets under it wrote smaller , maybe the card to be mate black with the writing in a gloss black or silver

Logo Text

hc . harbor cabinets

Font styles to use
Sans Serif
Script

Colors
1b1b1b
919191
f6f6f6
848484
ffc214
ec1f27

Requirements
Must have
• clean and simple , not too fussy ,
Nice to have
• n/a
Should not have
• n/a

```html
<!DOCTYPE html>
<html lang="en">
<head>
<meta charset="utf-8">
<title>Harbor Cabinets – Business Card</title>
<link href="https://fonts.googleapis.com/css2?family=Montserrat:wght@300;400;600&display=swap" rel="stylesheet">
<style>
  :root {
    --stage: #111111;
    --card: #1b1b1b;
    --card-edge: #262626;
    --silver: #c9c9c9;
    --silver-soft: #919191;
    --grey: #848484;
    --white: #f6f6f6;
  }
  * { margin: 0; padding: 0; box-sizing: border-box; }
  html, body {
    width: 1200px; height: 900px; overflow: hidden;
    background: var(--stage);
    font-family: "Montserrat", sans-serif;
  }
  .canvas {
    width: 1200px; height: 900px;
    display: flex; flex-direction: column;
    align-items: center; justify-content: center;
    gap: 44px;
  }
  .card {
    position: relative;
    width: 600px; height: 388px;
    background: var(--card);
    border: 1px solid var(--card-edge);
    border-radius: 24px;
  }

  /* brand name set as text */
  .brand {
    display: flex; align-items: center; gap: 14px;
    font-weight: 300; color: var(--silver);
    letter-spacing: 0.02em;
    white-space: nowrap;
  }
  .brand-mark {
    width: 14px; height: 14px;
    background: var(--silver);
  }

  /* front */
  .card-front .brand {
    position: absolute; left: 190px; top: 150px;
    font-size: 38px;
  }
  .card-front .brand .brand-mark { width: 18px; height: 18px; }
  .card-front .web {
    position: absolute; left: 222px; top: 236px;
    font-size: 15px; font-weight: 400;
    color: var(--silver-soft); letter-spacing: 0.04em;
  }

  /* back */
  .card-back .brand {
    position: absolute; left: 44px; top: 120px;
    font-size: 26px;
  }
  .details {
    position: absolute; left: 330px; top: 176px;
    color: var(--silver-soft);
    font-size: 13px; line-height: 1.55;
    letter-spacing: 0.03em;
  }
  .details .name {
    font-size: 19px; font-weight: 600;
    color: var(--white); letter-spacing: 0.14em;
    text-transform: uppercase; line-height: 1.2;
  }
  .details .role {
    font-size: 11px; font-weight: 400;
    color: var(--grey); letter-spacing: 0.16em;
    text-transform: uppercase; margin-bottom: 12px;
  }
  .details .address { color: var(--silver); font-weight: 600; margin-bottom: 10px; }
  .details .line { display: block; }
</style>
</head>
<body>
<main class="canvas">
  <section class="card card-front" aria-label="Card front">
    <div class="brand"><span class="brand-mark"></span>harbor cabinets</div>
    <div class="web">harborcabinets.co.uk</div>
  </section>

  <section class="card card-back" aria-label="Card back">
    <div class="brand"><span class="brand-mark"></span>harbor cabinets</div>
    <div class="details">
      <div class="name">Colin Fetterby</div>
      <div class="role">Managing Director</div>
      <div class="address">
        <span class="line">27 Moorgate Row</span>
        <span class="line">Kilbrannock, BT41 2QD</span>
      </div>
      <span class="line">harborcabinets.co.uk</span>
      <span class="line">07718492265</span>
    </div>
  </section>
</main>
</body>
</html>
```